Brivolo ( A new twist on task management )

We need modern, elegant, and clean (Quillon Design) on screens, buttons, and icons.

It is a (smart) task management application which helps the users to get notified and track task completion hassle free; Using notification profiles they create.

The interface of this application should be very simple and color schemes should be contemporary as long as they don’t make reading short text hard.

Following Quillon Design guidelines, the prefered font style is Roboto

Target Market(s)

Everyone from 13+

Industry/Entity Type

Software

Logo Text

Brivolo

Font styles to use
Other font styles liked:
• Roboto

```html
<!DOCTYPE html>
<html lang="en">
<head>
<meta charset="utf-8">
<title>Brivolo – Active Tasks</title>
<link rel="stylesheet" href="https://fonts.googleapis.com/css2?family=Roboto:wght@300;400;500&display=swap">
<style>
  :root {
    --status-blue: #74bfdd;
    --bar-blue: #85c9e6;
    --fab-blue: #85c9e6;
    --surface: #f4f4f4;
    --band: #f0f0f0;
    --card: #ffffff;
    --text: #555555;
    --text-soft: #8a8a8a;
    --icon: #8c8c8c;
    --nav: #000000;
    --white: #ffffff;
  }
  * { box-sizing: border-box; margin: 0; padding: 0; }
  html, body { width: 675px; height: 1200px; overflow: hidden; }
  body {
    position: relative;
    background: var(--surface);
    font-family: 'Roboto', sans-serif;
    color: var(--text);
  }
  .status-bar {
    position: absolute; left: 0; top: 0; width: 675px; height: 45px;
    background: var(--status-blue);
    display: flex; align-items: center; justify-content: flex-end;
    gap: 8px; padding-right: 16px; color: var(--white); font-size: 20px;
  }
  .app-bar {
    position: absolute; left: 0; top: 45px; width: 675px; height: 91px;
    background: var(--bar-blue);
    box-shadow: 0 2px 4px rgba(0,0,0,.12);
    z-index: 2;
  }
  .avatar {
    position: absolute; left: 25px; top: 33px; width: 58px; height: 58px;
    top: 33px; border-radius: 50%;
    background: radial-gradient(circle at 45% 40%, #b89a7a, #5b4a3c 70%, #2e3a44);
  }
  .app-bar .avatar { top: 33px; transform: translateY(-29px); }
  .user-name {
    position: absolute; left: 103px; top: 0; line-height: 91px;
    font-size: 25px; font-weight: 400; color: var(--white);
  }
  .filter-btn { position: absolute; left: 612px; top: 27px; }
  .section-band {
    position: absolute; left: 0; top: 136px; width: 675px; height: 71px;
    background: var(--band);
    text-align: center; line-height: 71px; font-size: 25px; color: var(--text);
  }
  .task-card {
    position: absolute; left: 25px; width: 625px; height: 79px;
    background: var(--card); border-radius: 3px;
    box-shadow: 0 1px 3px rgba(0,0,0,.16);
  }
  .task-card .play { position: absolute; left: 21px; top: 27px; }
  .task-title {
    position: absolute; left: 64px; top: 0; line-height: 79px;
    font-size: 24px; color: var(--text);
  }
  .icon-a { position: absolute; left: 525px; top: 26px; }
  .icon-b { position: absolute; left: 579px; top: 26px; }
  .running .stop { position: absolute; left: 21px; top: 27px; }
  .running .skip { position: absolute; left: 65px; top: 27px; }
  .running .task-title { left: 109px; top: 13px; line-height: 28px; }
  .timer {
    position: absolute; left: 109px; top: 45px;
    font-size: 17px; color: var(--text-soft);
  }
  .fab {
    position: absolute; top: 1007px; width: 77px; height: 77px; border-radius: 50%;
    background: var(--fab-blue);
    box-shadow: 0 2px 5px rgba(0,0,0,.2);
    display: flex; align-items: center; justify-content: center;
  }
  .fab-search { left: 26px; }
  .fab-add { left: 573px; }
  .nav-bar {
    position: absolute; left: 0; top: 1109px; width: 675px; height: 91px;
    background: var(--nav);
  }
  .nav-bar svg { position: absolute; top: 29px; }
</style>
</head>
<body>

<div class="status-bar">
  <svg width="26" height="20" viewBox="0 0 26 20"><path d="M13 19 0 4a20 20 0 0 1 26 0z" fill="#fff"/></svg>
  <svg width="20" height="20" viewBox="0 0 20 20"><path d="M20 0v20H0z" fill="#fff"/></svg>
  <svg width="13" height="22" viewBox="0 0 13 22"><rect x="0" y="3" width="13" height="19" fill="#fff"/><rect x="4" y="0" width="5" height="3" fill="#fff"/></svg>
  <span>12:30</span>
</div>

<header class="app-bar">
  <div class="avatar" role="img" aria-label="User profile photo"></div>
  <span class="user-name">Jalen Marrow</span>
  <svg class="filter-btn" width="38" height="38" viewBox="0 0 38 38" fill="none" stroke="#fff" stroke-width="2.2">
    <line x1="2" y1="8" x2="36" y2="8"/><circle cx="24" cy="8" r="3.5" fill="#85c9e6"/>
    <line x1="2" y1="19" x2="36" y2="19"/><circle cx="12" cy="19" r="3.5" fill="#85c9e6"/>
    <line x1="2" y1="30" x2="36" y2="30"/><circle cx="24" cy="30" r="3.5" fill="#85c9e6"/>
  </svg>
</header>

<div class="section-band">Active Tasks</div>

<svg width="0" height="0" style="position:absolute">
  <defs>
    <symbol id="i-play" viewBox="0 0 22 24"><path d="M1.5 1.5 20.5 12 1.5 22.5z" fill="none" stroke="#8c8c8c" stroke-width="1.8" stroke-linejoin="round"/></symbol>
    <symbol id="i-pin" viewBox="0 0 28 28"><path d="M16 2l10 10-3 1-5 5 1 4-2 2-5-5-8 8-1-1 8-8-5-5 2-2 4 1 5-5z" fill="#8c8c8c"/></symbol>
    <symbol id="i-place" viewBox="0 0 28 28"><path d="M14 2a7 7 0 0 0-7 7c0 5 7 12 7 12s7-7 7-12a7 7 0 0 0-7-7z" fill="#8c8c8c"/><circle cx="14" cy="9" r="2.6" fill="#fff"/><ellipse cx="14" cy="23" rx="12" ry="3.2" fill="none" stroke="#8c8c8c" stroke-width="1.8"/></symbol>
    <symbol id="i-clock" viewBox="0 0 28 28"><circle cx="14" cy="14" r="12.5" fill="none" stroke="#8c8c8c" stroke-width="1.6"/><path d="M14 6v8h6" fill="none" stroke="#8c8c8c" stroke-width="1.6"/></symbol>
  </defs>
</svg>

<main class="task-list">
  <div class="task-card" style="top:227px"><svg class="play" width="22" height="24"><use href="#i-play"/></svg><span class="task-title">Task 1</span><svg class="icon-a" width="28" height="28"><use href="#i-pin"/></svg><svg class="icon-b" width="28" height="28"><use href="#i-place"/></svg></div>
  <div class="task-card" style="top:317px"><svg class="play" width="22" height="24"><use href="#i-play"/></svg><span class="task-title">Task 2</span><svg class="icon-a" width="28" height="28"><use href="#i-pin"/></svg><svg class="icon-b" width="28" height="28"><use href="#i-place"/></svg></div>
  <div class="task-card" style="top:407px"><svg class="play" width="22" height="24"><use href="#i-play"/></svg><span class="task-title">Task 3</span><svg class="icon-a" width="28" height="28"><use href="#i-clock"/></svg><svg class="icon-b" width="28" height="28"><use href="#i-place"/></svg></div>
  <div class="task-card" style="top:497px"><svg class="play" width="22" height="24"><use href="#i-play"/></svg><span class="task-title">Task 4</span><svg class="icon-a" width="28" height="28"><use href="#i-pin"/></svg><svg class="icon-b" width="28" height="28"><use href="#i-place"/></svg></div>
  <div class="task-card" style="top:587px"><svg class="play" width="22" height="24"><use href="#i-play"/></svg><span class="task-title">Task 5</span><svg class="icon-b" width="28" height="28"><use href="#i-clock"/></svg></div>
  <div class="task-card" style="top:677px"><svg class="play" width="22" height="24"><use href="#i-play"/></svg><span class="task-title">Task 6</span><svg class="icon-a" width="28" height="28"><use href="#i-pin"/></svg><svg class="icon-b" width="28" height="28"><use href="#i-place"/></svg></div>
  <div class="task-card running" style="top:767px">
    <svg class="stop" width="26" height="26" viewBox="0 0 26 26"><rect width="26" height="26" rx="2" fill="#8c8c8c"/></svg>
    <svg class="skip" width="28" height="26" viewBox="0 0 28 26"><path d="M0 0 20 13 0 26z" fill="#8c8c8c"/><rect x="23" y="0" width="3" height="26" fill="#8c8c8c"/></svg>
    <span class="task-title">Task 7</span>
    <span class="timer">00h:15m:56s</span>
    <svg class="icon-b" width="28" height="28"><use href="#i-place"/></svg>
  </div>
</main>

<div class="fab fab-search">
  <svg width="26" height="26" viewBox="0 0 26 26" fill="none" stroke="#fff" stroke-width="2"><circle cx="11" cy="11" r="8"/><line x1="17" y1="17" x2="24" y2="24"/></svg>
</div>
<div class="fab fab-add">
  <svg width="26" height="26" viewBox="0 0 26 26" stroke="#fff" stroke-width="2"><line x1="13" y1="1" x2="13" y2="25"/><line x1="1" y1="13" x2="25" y2="13"/></svg>
</div>

<nav class="nav-bar">
  <svg style="left:133px" width="34" height="34" viewBox="0 0 34 34"><path d="M30 3 4 17 30 31z" fill="none" stroke="#fff" stroke-width="3" stroke-linejoin="round"/></svg>
  <svg style="left:320px" width="34" height="34" viewBox="0 0 34 34"><circle cx="17" cy="17" r="15" fill="none" stroke="#fff" stroke-width="3"/></svg>
  <svg style="left:509px" width="32" height="32" viewBox="0 0 32 32"><rect x="2" y="2" width="28" height="28" fill="none" stroke="#fff" stroke-width="3"/></svg>
</nav>

</body>
</html>
```